Redesign Of Current Landing Page

I need to redesign this landing page https://www.bluewillowpromos.example/?page=landing&landing=23 (Please do not opt in because when you do it will show you the home page. Please clear your cookies before going to this url above to view the 1 page landing page.)

Please use my updated website as a reference for colors and logo.
http://sitecraftorly.example/dh/bwpg/index.html

I would like the call to action to be a button that opens into a lead form...

Button would be "Download Samples"

Target Market(s)

small business owners

Industry/Entity Type

Marketing

Number of Pages Required

1 page

Colors

Designer to choose colors to be used in the design.

Requirements
Must have
• must be full responsive on all devices
Nice to have
• must have a legitimate professional apeal to it
Should not have
• open

```html
<!DOCTYPE html>
<html lang="en">
<head>
<meta charset="utf-8">
<title>Blue Willow Promos — Landing</title>
<link rel="stylesheet" href="https://fonts.googleapis.com/css2?family=Montserrat:wght@400;600;700&family=Open+Sans:ital,wght@0,400;0,600;0,700;1,400&display=swap">
<style>
:root{
  --navy:#0b1733;
  --navy-2:#10204a;
  --blue:#1767c4;
  --blue-light:#2d86e0;
  --orange:#f6a609;
  --ink:#1c1c1c;
  --grey-text:#6b6b6b;
  --light:#ececec;
  --dark:#1a1d22;
  --white:#fff;
}
*{box-sizing:border-box;margin:0;padding:0}
html,body{width:1200px;height:3797px;overflow:hidden}
body{font-family:"Open Sans",Arial,sans-serif;color:var(--ink);background:var(--white);font-size:12px}
h1,h2,h3,h4,.btn,.nav a{font-family:"Montserrat",Arial,sans-serif}
.wrap{width:750px;margin:0 auto;position:relative;height:100%}
section,header,footer{position:relative;width:1200px;overflow:hidden}
.btn{display:inline-block;color:var(--white);font-weight:700;font-size:10px;letter-spacing:.5px;text-transform:uppercase;padding:0 22px;height:34px;line-height:34px;border-radius:2px;text-decoration:none;white-space:nowrap}
.btn-orange{background:var(--orange)}
.btn-blue{background:var(--blue)}

/* top bar + nav */
.topbar{height:25px;background:var(--navy);color:#cfd6e6;font-size:10px}
.topbar .wrap{display:flex;align-items:center;justify-content:space-between}
.topbar b{color:var(--white)}
.topbar .right{display:flex;gap:10px;align-items:center}
.topbar .dot{width:8px;height:8px;border-radius:50%;background:#5a6b90;display:inline-block}
.nav{height:59px;background:var(--navy-2)}
.nav .wrap{display:flex;align-items:center;justify-content:space-between}
.brand{display:flex;align-items:center;gap:8px;color:var(--white);font-family:"Montserrat",sans-serif;font-weight:700;font-size:16px;letter-spacing:.5px}
.brand .sq{width:26px;height:26px;background:var(--blue-light)}
.nav ul{list-style:none;display:flex;gap:16px}
.nav a{color:#d9e0ef;font-size:9px;font-weight:600;text-decoration:none;text-transform:uppercase}
.nav a.on{color:var(--white);border-bottom:2px solid var(--blue-light);padding-bottom:4px}

/* hero */
.hero{height:397px}
.hero-photo{position:absolute;inset:0;background:linear-gradient(180deg,#1d6fd0 0%,#3d92e8 45%,#9fcaf2 75%,#dfe7ef 100%)}
.hero-copy{position:absolute;left:0;top:60px;color:var(--white)}
.hero-copy h1{font-weight:400;font-size:26px;line-height:32px;text-shadow:0 1px 3px rgba(0,0,0,.3)}
.hero-copy h1 .hl{color:var(--orange);font-weight:700}
.hero-copy .btn{margin-top:24px}
.lead-form{position:absolute;right:0;top:93px;width:242px;height:304px;background:var(--white);padding:16px 18px;box-shadow:0 4px 14px rgba(0,0,0,.2)}
.lead-form .kick{color:var(--blue);font-weight:700;font-size:11px;font-family:"Montserrat",sans-serif}
.lead-form h3{font-size:21px;font-weight:700;margin-bottom:14px}
.field{border-bottom:1px solid #bfc6d2;height:32px;font-size:9px;color:#666;padding-top:4px;margin-bottom:8px}
.field span{display:block;font-size:11px;color:var(--ink);margin-top:2px}
.lead-form .btn{width:100%;text-align:center;margin-top:10px;height:30px;line-height:30px}
.lead-form p{font-size:9px;color:#777;margin-top:10px;line-height:13px}
.lead-form:target{box-shadow:0 0 0 3px var(--orange),0 4px 14px rgba(0,0,0,.2)}

/* clients */
.clients{height:109px;background:var(--light)}
.clients .wrap{display:flex;align-items:center;justify-content:space-between;padding:0 40px}
.clients span{font-family:"Montserrat",sans-serif;font-weight:700;font-size:15px;color:#5d5d5d}

/* three ways */
.ways{height:499px;text-align:center}
.ways .eyebrow{padding-top:50px;font-size:10px;font-weight:700;letter-spacing:2px;text-transform:uppercase}
.ways h2{color:var(--blue);font-size:29px;font-weight:700;letter-spacing:3px;margin-top:6px}
.way-row{display:flex;justify-content:space-between;margin-top:44px;position:relative}
.way{width:200px}
.way .circ{width:92px;height:92px;border-radius:50%;margin:0 auto;display:flex;align-items:center;justify-content:center;border:5px solid #e3e9f2}
.way .circ.blue{background:var(--blue)}
.way .circ.black{background:#161616}
.way h4{font-size:12px;letter-spacing:1px;margin-top:20px}
.way h4.blue{color:var(--blue)}
.way p{font-size:9px;color:var(--grey-text);line-height:13px;margin-top:8px}
.way-arrow{position:absolute;top:30px}
.ways .btn{margin-top:34px}

/* model */
.model{height:531px;background:linear-gradient(180deg,#22262d,#2c3038 60%,#1f2228);color:var(--white);text-align:center}
.model .eyebrow{padding-top:60px;font-size:10px;letter-spacing:2px;font-weight:700;color:#cfd3da}
.model h2{font-size:25px;letter-spacing:2px;margin-top:4px}
.phone{position:absolute;left:50%;margin-left:-95px;top:160px;width:190px;height:340px;border-radius:26px;background:linear-gradient(180deg,#f3f4f6,#dfe2e8)}
.feat{position:absolute;font-size:9px;line-height:13px;color:#d4d8df}
.feat h4{font-size:11px;color:var(--white);letter-spacing:1px;margin-bottom:4px}
.feat.left{text-align:right}
.feat.right{text-align:left}
.icon-circ{position:absolute;width:50px;height:50px;border-radius:50%;background:var(--blue);display:flex;align-items:center;justify-content:center}

/* video */
.video{height:451px;background:#eeeeee}
.laptop{position:absolute;left:0;top:46px;width:440px}
.laptop .screen{height:258px;background:linear-gradient(135deg,#2a3340,#4b5a6d 55%,#7e8da0);border:8px solid #1e1e1e;border-radius:8px 8px 0 0}
.laptop .base{height:12px;background:#cfd2d6;margin:0 -24px;border-radius:0 0 10px 10px}
.video-copy{position:absolute;left:488px;top:52px;width:262px;border-left:2px solid var(--orange);padding-left:14px}
.video-copy h3{font-size:15px;letter-spacing:2px;font-weight:600}
.video-copy .save{display:flex;align-items:center;gap:8px;font-family:"Montserrat",sans-serif;font-weight:700;font-size:23px;letter-spacing:2px;margin-top:4px}
.badge{width:60px;height:60px;border-radius:50%;background:var(--blue);color:var(--white);display:flex;align-items:center;justify-content:center;font-size:19px;letter-spacing:0}
.video-copy h5{font-size:10px;margin-top:18px;font-weight:700}
.video-copy p{font-size:9px;color:var(--grey-text);line-height:13px;margin-top:10px}
.video-btns{position:absolute;left:142px;top:380px;display:flex;gap:22px}

/* incentives */
.incent{height:436px;background:linear-gradient(180deg,#2a2d33,#1f2126);color:var(--white);text-align:center}
.incent h2{font-size:27px;letter-spacing:3px;padding-top:58px}
.cards{display:flex;justify-content:space-between;margin-top:36px}
.card{width:168px}
.card .ph{height:110px}
.card .lab{background:var(--blue);height:34px;display:flex;align-items:center;justify-content:center;padding:0 10px;line-height:11px;font-size:8px;font-weight:700;letter-spacing:.5px;font-family:"Montserrat",sans-serif}
.incent .btn{margin-top:42px}

/* brochure */
.brochure{height:379px}
.brochure h2{position:absolute;left:0;top:48px;font-size:22px;letter-spacing:2px;line-height:28px}
.brochure h2 small{display:block;font-size:19px}
.brochure .txt{position:absolute;left:0;top:122px;width:300px;font-size:9px;color:var(--grey-text);line-height:13px}
.brochure .txt p{margin-bottom:12px}
.brochure .btn{position:absolute;left:0;top:260px}
.brochure-art{position:absolute;left:395px;top:50px;width:355px;height:270px;background:linear-gradient(160deg,#f5f5f5,#d8d8d8 60%,#b9b9b9);transform:skewY(-6deg)}

/* testimonial */
.quote{height:190px;background:var(--blue);color:var(--white)}
.quote .avatar{position:absolute;left:368px;top:52px;width:46px;height:46px;border-radius:50%;background:linear-gradient(#8fc4f0,#4b8fd0);border:3px solid var(--white)}
.quote .who{position:absolute;left:360px;top:112px;font-size:9px;font-weight:700;text-align:center;width:62px}
.quote .who small{display:block;font-weight:400;font-size:8px}
.quote blockquote{position:absolute;left:462px;top:58px;width:420px;font-style:italic;font-size:11px;line-height:16px}

/* reseller cta */
.reseller{height:208px;text-align:center}
.reseller h2{font-family:"Open Sans",sans-serif;font-style:italic;font-weight:400;font-size:22px;line-height:26px;padding-top:44px;color:#333}
.reseller .btn{margin-top:22px;padding:0 40px;height:40px;line-height:40px}

/* address */
.address{height:349px;background:#f1f1f1}
.map{position:absolute;left:0;top:0;width:722px;height:349px;background:linear-gradient(135deg,#e9e6df,#d9d6cf 50%,#e4e1da)}
.addr{position:absolute;left:738px;top:36px;width:230px}
.addr h3{font-family:"Open Sans",sans-serif;font-weight:400;font-size:22px}
.addr hr{border:0;border-top:1px solid #cfcfcf;margin:10px 0 14px}
.addr .row{display:flex;gap:10px;font-size:9px;color:#444;line-height:13px;margin-bottom:16px}
.addr .row svg{flex:none;margin-top:2px}

/* footer */
footer{height:164px;background:var(--dark);color:#cfd3da}
footer .wrap{display:flex;padding-top:34px}
footer h4{font-family:"Open Sans",sans-serif;font-weight:400;font-size:13px;color:var(--white);margin-bottom:8px}
footer .info{width:472px}
footer .links{display:grid;grid-template-columns:repeat(3,1fr);font-size:8px;line-height:13px;color:#a8adb6}
footer .social{width:170px;font-size:8px;color:#a8adb6}
footer .social .dots{display:flex;gap:8px;margin-top:6px}
footer .social .dots i{width:11px;height:11px;border-radius:50%;background:#cfd3da;display:block}
footer .legal{font-size:8px;line-height:12px;color:#a8adb6}
</style>
</head>
<body>

<header class="topbar">
  <div class="wrap">
    <div>USA Office: <b>619-555-0142</b> &nbsp;|&nbsp; International: <b>1-800-555-0199</b></div>
    <div class="right"><span class="dot"></span><span class="dot"></span><span class="dot"></span><span>LOGIN</span><span>SIGN UP</span></div>
  </div>
</header>
<header class="nav">
  <div class="wrap">
    <div class="brand"><span class="sq"></span>Blue Willow Promos</div>
    <ul>
      <li><a class="on">Home</a></li><li><a>Our Incentives</a></li><li><a>Samples</a></li><li><a>How It Works</a></li><li><a>Testimonials</a></li><li><a>FAQ</a></li><li><a>Contact</a></li>
    </ul>
  </div>
</header>

<section class="hero">
  <div class="hero-photo" role="img" aria-label="Happy couple travelling with luggage beside a passenger jet in a blue sky"></div>
  <div class="wrap">
    <div class="hero-copy">
      <h1>Create Unlimited Giveaways<br>Boost Sales At Just $99/mo<br><span class="hl">30 Day Risk Free Trial</span></h1>
      <a class="btn btn-orange" href="#lead-form">Download Samples</a>
    </div>
    <form class="lead-form" id="lead-form">
      <div class="kick">SIGN UP RISK FREE FOR 30 DAYS</div>
      <h3>RIGHT NOW!</h3>
      <div class="field">Your full name<span>Leo</span></div>
      <div class="field">Your email</div>
      <div class="field">Your phone</div>
      <a class="btn btn-blue">Submit Here</a>
      <p>Our team will answer to get back to you within 24 hours.</p>
    </form>
  </div>
</section>

<section class="clients">
  <div class="wrap">
    <span>Hartwell Realty</span><span>HomeCart</span><span>Kanto Motors</span><span>Skyline TV</span><span>Evergreen Mutual</span>
  </div>
</section>

<section class="ways">
  <div class="wrap">
    <div class="eyebrow">Give away unlimited incentives to your customers</div>
    <h2>THREE EASY WAYS !</h2>
    <div class="way-row">
      <svg class="way-arrow" style="left:196px" width="80" height="30" viewBox="0 0 80 30"><path d="M4 22 Q40 2 72 16" fill="none" stroke="#aaa" stroke-width="2"/><path d="M64 10 L74 17 L63 21" fill="none" stroke="#aaa" stroke-width="2"/></svg>
      <svg class="way-arrow" style="left:474px" width="80" height="30" viewBox="0 0 80 30"><path d="M4 22 Q40 2 72 16" fill="none" stroke="#aaa" stroke-width="2"/><path d="M64 10 L74 17 L63 21" fill="none" stroke="#aaa" stroke-width="2"/></svg>
      <div class="way">
        <div class="circ blue"><svg width="36" height="34" viewBox="0 0 36 34" fill="none" stroke="#fff" stroke-width="2.4"><rect x="9" y="2" width="18" height="9"/><rect x="3" y="11" width="30" height="14" rx="2"/><rect x="9" y="20" width="18" height="12" fill="#1767c4"/></svg></div>
        <h4>PRINT</h4>
        <p>Download PDF certificates to print and hand them out or mail them to your customers!</p>
      </div>
      <div class="way">
        <div class="circ black"><svg width="38" height="32" viewBox="0 0 38 32" fill="none" stroke="#fff" stroke-width="2.2"><rect x="2" y="2" width="34" height="28" rx="2"/><line x1="2" y1="9" x2="36" y2="9"/><line x1="8" y1="16" x2="30" y2="16"/><line x1="8" y1="22" x2="24" y2="22"/></svg></div>
        <h4 class="blue">FROM YOUR WEBSITE</h4>
        <p>Place our HTML banners on your homepage. Your customers click the banner to get their certificate, we email you their contact info. 100% lead automation!</p>
      </div>
      <div class="way">
        <div class="circ blue"><svg width="38" height="28" viewBox="0 0 38 28" fill="none" stroke="#fff" stroke-width="2.4"><rect x="2" y="2" width="34" height="24" rx="2"/><path d="M2 3 L19 16 L36 3"/></svg></div>
        <h4>E-MAIL</h4>
        <p>Email certificates to your customers with one click!</p>
      </div>
    </div>
    <a class="btn btn-orange">Request A Call</a>
  </div>
</section>

<section class="model">
  <div class="wrap">
    <div class="eyebrow">BWPG PLUGS INTO</div>
    <h2>YOUR BUSINESS MODEL 4 WAYS</h2>
    <div class="phone" role="img" aria-label="Smartphone showing sales charts on its screen"></div>

    <div class="feat left" style="top:208px;width:160px;left:20px"><h4>ADVERTISING</h4>Download PDF certificates to print and hand them out or mail them to your customers!</div>
    <div class="icon-circ" style="left:193px;top:212px"><svg width="24" height="22" viewBox="0 0 24 22" fill="#fff"><path d="M2 8h5l10-6v18L7 14H2z"/></svg></div>
    <div class="feat left" style="top:300px;width:160px;left:20px"><h4>SALES</h4>Now that you have generated the lead, try enticing a prospect with an upgrade and offer them two nights plus airfare when they purchase today. There are so many ways to close a deal by offering our incentives.</div>
    <div class="icon-circ" style="left:193px;top:304px"><svg width="24" height="22" viewBox="0 0 24 22" fill="#fff"><rect x="2" y="14" width="4" height="7"/><rect x="9" y="9" width="4" height="12"/><rect x="16" y="3" width="4" height="18"/></svg></div>

    <div class="icon-circ" style="left:507px;top:212px"><svg width="22" height="24" viewBox="0 0 22 24" fill="#fff"><circle cx="11" cy="7" r="5"/><path d="M2 23c0-6 4-9 9-9s9 3 9 9z"/></svg></div>
    <div class="feat right" style="top:208px;width:160px;right:20px"><h4>RESIDUAL BUSINESS</h4>Contact all of your past clients and offer them a two night getaway as a customer loyalty gesture to motivate repeat business!</div>
    <div class="icon-circ" style="left:507px;top:304px"><svg width="24" height="24" viewBox="0 0 24 24" fill="none" stroke="#fff" stroke-width="2.4"><path d="M10 14 L14 10"/><rect x="2" y="12" width="10" height="6" rx="3" transform="rotate(-45 7 15)"/><rect x="12" y="6" width="10" height="6" rx="3" transform="rotate(-45 17 9)"/></svg></div>
    <div class="feat right" style="top:300px;width:160px;right:20px"><h4>REFERRALS</h4>Contact all of your past customers and offer a deluxe getaway package to anyone who refers a new client to you. Or at the end of your sales presentation, offer a reward.</div>
  </div>
</section>

<section class="video">
  <div class="wrap">
    <div class="laptop">
      <div class="screen" role="img" aria-label="Presenter in a suit speaking in a promotional video"></div>
      <div class="base"></div>
    </div>
    <div class="video-copy">
      <h3>WATCH VIDEO TO</h3>
      <div class="save">SAVE <span class="badge">20%</span> TODAY</div>
      <h5>Separate Redemption Websites with Online Reservation Systems</h5>
      <p>First and foremost we're a marketing company, so we want to protect the integrity of your promotions.</p>
      <p>We allow you to brand the certificates with your company info. On every certificate there is a "Compliments Of" area where we allow you to put up to 3 lines of text and a logo.</p>
    </div>
    <div class="video-btns">
      <a class="btn btn-orange">Take A Quick Tour Of Our Incentives</a>
      <a class="btn btn-blue">View &amp; Redeem Samples</a>
    </div>
  </div>
</section>

<section class="incent">
  <div class="wrap">
    <h2>OUR INCENTIVES</h2>
    <div class="cards">
      <div class="card"><div class="ph" role="img" aria-label="Smiling traveller with a certificate" style="background:linear-gradient(135deg,#f0e6dc,#c9a98c)"></div><div class="lab">VACATION CERTIFICATES</div></div>
      <div class="card"><div class="ph" role="img" aria-label="Pile of phones and tablets" style="background:linear-gradient(135deg,#4a5a70,#22303e)"></div><div class="lab">ELECTRONIC PRODUCT<br>CERTIFICATES</div></div>
      <div class="card"><div class="ph" role="img" aria-label="Chef plating a dish in a kitchen" style="background:linear-gradient(135deg,#e6e2dc,#8f8a84)"></div><div class="lab">DINING CERTIFICATES</div></div>
      <div class="card"><div class="ph" role="img" aria-label="Hand holding a fuel pump nozzle" style="background:linear-gradient(135deg,#7da84a,#3c5a24)"></div><div class="lab">GAS &amp; GROCERY REBATE<br>CERTIFICATES</div></div>
    </div>
    <a class="btn btn-orange">Request Free Sample Package</a>
  </div>
</section>

<section class="brochure">
  <div class="wrap">
    <h2><small>VIEW OUR</small>ONLINE BROCHURE</h2>
    <div class="txt">
      <p>Browse every incentive we offer in one place, with pricing, sample certificates and ideas for how each one can help you close more sales and reward loyal clients.</p>
      <p>Flip through the pages online or download a copy to share with your team, then pick the giveaways that best fit your customers and your budget.</p>
    </div>
    <a class="btn btn-orange">Click Here Now</a>
    <div class="brochure-art" role="img" aria-label="Open printed brochure showing home photos"></div>
  </div>
</section>

<section class="quote">
  <div class="avatar" role="img" aria-label="Customer portrait"></div>
  <div class="who">DANA R.<small>Prescott, AZ</small></div>
  <blockquote>A wonderful, innovative way to shop for your dining experiences and a great way to save money at your favorite restaurants! It is a simple and easy method to redeem your restaurant certificates.</blockquote>
</section>

<section class="reseller">
  <h2>Know Any Businesses That Could Benefit Using Incentives<br>To Bring In More Customers?</h2>
  <a class="btn btn-orange">Click Here To Learn More About Our Reseller Program!</a>
</section>

<section class="address">
  <div class="map" role="img" aria-label="Street map with the office location marked"></div>
  <div class="addr">
    <h3>Our Address</h3>
    <hr>
    <div class="row"><svg width="10" height="14" viewBox="0 0 10 14"><path d="M5 0a5 5 0 0 1 5 5c0 4-5 9-5 9S0 9 0 5a5 5 0 0 1 5-5z" fill="#1767c4"/><circle cx="5" cy="5" r="2" fill="#fff"/></svg><div>Blue Willow Promotions Group, Inc.<br>1420 Harbor Avenue<br>San Diego CA 92101</div></div>
    <div class="row"><svg width="12" height="12" viewBox="0 0 12 12"><path d="M2 1h3l1 3-2 1a7 7 0 0 0 3 3l1-2 3 1v3c0 1-1 1-1 1C5 11 1 7 1 2c0 0 0-1 1-1z" fill="#1767c4"/></svg><div>619-555-0142<br>1-800-555-0199</div></div>
    <div class="row"><svg width="12" height="12" viewBox="0 0 12 12"><circle cx="6" cy="6" r="5" fill="none" stroke="#1767c4" stroke-width="1.6"/><path d="M6 3v3l2 1" stroke="#1767c4" stroke-width="1.4" fill="none"/></svg><div>Hours: Mon-Fri 7am - 4pm PST<br>Sat-Sun CLOSED</div></div>
  </div>
</section>

<footer>
  <div class="wrap">
    <div class="info">
      <h4>Information</h4>
      <div class="links">
        <div>Our Incentives<br>Samples<br>Affiliate<br>Testimonials</div>
        <div>Faq<br>Contact Us<br>Terms &amp; Conditions<br>Privacy Policy</div>
        <div>Affiliate Program<br>Terms &amp; Conditions<br>Privacy Policy<br>Login</div>
      </div>
    </div>
    <div class="social">
      <h4>Social Networks</h4>
      Join the conversation
      <div class="dots"><i></i><i></i><i></i><i></i></div>
    </div>
    <div class="legal">
      <h4>Legal Stuff</h4>
      Copyright © 2017<br>Blue Willow Promotions<br>Group, Inc.<br>All Rights Reserved
    </div>
  </div>
</footer>

</body>
</html>
```